Sample Book Covers University Press

We need three (simple) sample book FRONT covers designed, which will represent the look and feel of a new university press. This institution is a leader in Depth Psychology, Mythology and Humanities.

The covers should use the same template, font etc.
Each cover will have a different color font and a different image.

Please see attached document for text.
Font: Close to Pacifica Font attached, this should also be one of the colors.
Other font colors green and blue, which can be different from the ones in the document.

Back round color should be close to the sample, or the the attached file.

These will be sample files, we will not use them on actual books, so feel free to use other images representing the categories. (or the ones in the image)

Questions? Please feel free to contact us.

University

```html
<!DOCTYPE html>
<html lang="en">
<head>
<meta charset="utf-8">
<title>Depth Psychology — Book Cover</title>
<link href="https://fonts.googleapis.com/css2?family=Tinos&display=swap" rel="stylesheet">
<style>
  :root {
    --sand: #e6c97b;
    --forest: #063f04;
    --ink: #0b4a0a;
    --paper: #ffffff;
    --stone-pale: #c4cec0;
    --stone-light: #a9b5a4;
    --stone-mid: #8d9a8a;
    --stone-sage: #75846f;
    --stone-dark: #3f4150;
    --stone-shadow: #2c2e3a;
  }
  html, body {
    margin: 0;
    padding: 0;
    width: 800px;
    height: 1200px;
    overflow: hidden;
    background: var(--paper);
  }
  .cover {
    position: relative;
    width: 800px;
    height: 1200px;
    font-family: "Tinos", "Times New Roman", serif;
  }
  .title-band {
    position: absolute;
    top: 0;
    left: 0;
    width: 800px;
    height: 392px;
    background: var(--sand);
  }
  .book-title {
    position: absolute;
    top: 130px;
    left: 0;
    width: 800px;
    margin: 0;
    text-align: center;
    color: var(--ink);
    font-weight: 400;
    font-size: 108px;
    line-height: 86px;
    letter-spacing: -3px;
  }
  .divider {
    position: absolute;
    top: 392px;
    left: 0;
    width: 800px;
    height: 24px;
    background: var(--forest);
  }
  .cover-art {
    position: absolute;
    top: 416px;
    left: 0;
    width: 800px;
    height: 570px;
    background:
      radial-gradient(ellipse 260px 120px at 560px 470px, rgba(44,46,58,0.75) 0%, rgba(44,46,58,0) 100%),
      radial-gradient(ellipse 160px 260px at 690px 260px, rgba(63,65,80,0.7) 0%, rgba(63,65,80,0) 100%),
      radial-gradient(ellipse 220px 90px at 330px 400px, rgba(63,65,80,0.45) 0%, rgba(63,65,80,0) 100%),
      radial-gradient(ellipse 180px 160px at 300px 150px, rgba(196,206,192,0.8) 0%, rgba(196,206,192,0) 100%),
      radial-gradient(ellipse 160px 150px at 540px 150px, rgba(196,206,192,0.6) 0%, rgba(196,206,192,0) 100%),
      linear-gradient(180deg, var(--stone-light) 0%, var(--stone-mid) 45%, var(--stone-sage) 75%, var(--stone-mid) 100%);
  }
  .publisher-band {
    position: absolute;
    top: 986px;
    left: 0;
    width: 800px;
    height: 214px;
    background: var(--forest);
  }
  .publisher-name {
    position: absolute;
    top: 1064px;
    left: 0;
    width: 800px;
    margin: 0;
    text-align: center;
    color: var(--paper);
    font-weight: 400;
    font-size: 58px;
    line-height: 60px;
  }
</style>
</head>
<body>
  <div class="cover">
    <div class="title-band"></div>
    <h1 class="book-title">DEPTH<br>PSYCHOLOGY</h1>
    <div class="divider"></div>
    <div class="cover-art" role="img" aria-label="Carved stone relief of a multi-faced head in grey-green tones with deep shadows"></div>
    <div class="publisher-band"></div>
    <p class="publisher-name">Meridian Press</p>
  </div>
</body>
</html>
```